Music Artist Needs Flyer Design ASAP

Looking for a flyer design to promote for artist release party. Music artist is mainly hip hop based. We would like designs that are simple, creative and eye catching.

Requirements
Must have
• The flyer must have the photo of the artist I attached incorporated into the design. Must say "Free ZUKO" Release Party, Live at Tolly's Bar Thursday Dec.27 2012 (artist name=ZUKO VeN), show starts at 8pm, No cover charge, 21 and over, Register to Win Coral Blaze tickets Giveaway

```html
<!DOCTYPE html>
<html lang="en">
<head>
<meta charset="utf-8">
<title>Free ZUKO Release Party</title>
<link rel="stylesheet" href="https://fonts.googleapis.com/css2?family=Dosis:wght@300;400;500;600;700&family=Ubuntu:wght@300&display=swap">
<style>
  :root {
    --paper: #e5e8e6;
    --frame: #232323;
    --band: rgba(178, 28, 36, 0.93);
    --deep-red: #a0131a;
    --ink: #161616;
    --blush: #f3c9cb;
    --photo-a: #3a2a7a;
    --photo-b: #d9a02a;
    --photo-c: #c53a1e;
  }
  html, body { margin: 0; padding: 0; overflow: hidden; }
  body { width: 960px; height: 1200px; background: var(--paper); }
  .flyer { position: relative; width: 960px; height: 1200px; overflow: hidden; background: var(--paper); font-family: "Dosis", sans-serif; }
  .frame { position: absolute; left: 60px; top: 60px; width: 840px; height: 1080px; background: var(--frame); }
  .texture { position: absolute; left: 60px; top: 220px; width: 110px; height: 760px;
    background: linear-gradient(180deg, rgba(120,120,120,0.35), rgba(90,90,90,0.12)); }
  .band { position: absolute; background: var(--band); }
  .band > span { position: absolute; top: 0; white-space: nowrap; }
  .title-band { left: 0; top: 72px; width: 832px; height: 142px; }
  .free { position: absolute; left: 64px; top: 86px; font-size: 84px; font-weight: 500; color: var(--ink); line-height: 1; }
  .artist { position: absolute; left: 238px; top: 60px; font-size: 156px; font-weight: 700; color: var(--deep-red);
    -webkit-text-stroke: 2px var(--ink); line-height: 1; }
  .release { position: absolute; left: 623px; top: 70px; font-family: "Ubuntu", sans-serif; font-weight: 300;
    font-size: 33px; line-height: 33px; color: var(--blush); }
  .release span { display: block; }
  .release span:nth-child(3) { opacity: .85; }
  .release span:nth-child(4) { opacity: .7; }
  .photo { position: absolute; left: 174px; top: 232px; width: 650px; height: 488px;
    background: radial-gradient(circle at 50% 45%, var(--photo-b) 0%, var(--photo-c) 45%, var(--photo-a) 100%); }
  .spaced { font-weight: 400; font-size: 28px; letter-spacing: 19px; color: var(--ink); line-height: 60px; }
  .hi { font-weight: 600; color: var(--deep-red); -webkit-text-stroke: 1.2px var(--ink); }
  .venue { left: 172px; top: 736px; width: 788px; height: 62px; }
  .venue .spaced { left: 128px; line-height: 62px; }
  .venue .hi { left: 340px; font-size: 60px; line-height: 62px; }
  .date { left: 0; top: 818px; width: 828px; height: 60px; }
  .date .day { left: 172px; font-size: 38px; font-variant: small-caps; color: var(--ink); line-height: 60px; }
  .date .hi { left: 320px; font-size: 58px; line-height: 60px; }
  .date .year { left: 655px; font-size: 42px; color: var(--ink); line-height: 60px; }
  .time { left: 172px; top: 896px; width: 788px; height: 60px; }
  .time .spaced { left: 74px; }
  .time .hi { left: 524px; font-size: 60px; line-height: 60px; }
  .time .hi small { font-size: 44px; }
  .entry { left: 0; top: 978px; width: 828px; height: 60px; }
  .entry .cover { left: 174px; font-size: 56px; font-variant: small-caps; letter-spacing: 8px; color: var(--ink); line-height: 60px; }
  .entry .age { left: 628px; font-size: 60px; color: var(--ink); line-height: 64px; }
  .prize { left: 60px; top: 1084px; width: 842px; height: 56px; }
  .prize .line { left: 4px; font-size: 34px; line-height: 56px; font-weight: 500; letter-spacing: 3px; color: var(--deep-red); -webkit-text-stroke: .6px var(--ink); }
</style>
</head>
<body>
<div class="flyer">
  <div class="frame"></div>
  <div class="texture" role="img" aria-label="Faint grey graffiti lettering of the artist name"></div>

  <div class="band title-band"></div>
  <div class="free">Free</div>
  <div class="artist">ZUKO</div>
  <div class="release"><span>release party</span><span>release party</span><span>release party</span><span>release party</span></div>

  <div class="photo" role="img" aria-label="Photo of the artist ZUKO standing in front of a colourful graffiti wall"></div>

  <div class="band venue"><span class="spaced">live at</span><span class="hi">Tolly's Bar</span></div>
  <div class="band date"><span class="day">Thursday</span><span class="hi">DECEMBER 27,</span><span class="year">2012</span></div>
  <div class="band time"><span class="spaced">show starts at</span><span class="hi">8<small>PM</small></span></div>
  <div class="band entry"><span class="cover">No Cover</span><span class="age">21+</span></div>
  <div class="band prize"><span class="line">Enter for a chance to win Coral Blaze Tickets</span></div>
</div>
</body>
</html>
```